LUSTRIA INC. is a new Fashion Stylist, Design Merchandiser, and consultant in the fashion industry

We need a logo design for a new Calgary, Alberta based company that is in the business of making over your image, wardrobe and style for both business and personal purposes.

Target Market(s)

Professional female and male business people looking for a new style or complete fashion makeover including clothes closet merchandising and makeover.

Contact Information for Business Card

Number of Pages Required

1 page

Font styles to use
Script

Colors
fac994
fbe7d2
fee3d4

Requirements
Must have
• Fashion Industry theme that is very elegant and colorful using gold/bronze/silver color themes.
Nice to have
• Incorporate the company name with the creative font to come up with the appropriate "logo"

```html
<!DOCTYPE html>
<html lang="en">
<head>
<meta charset="utf-8">
<title>Lustria Inc. — Business Card</title>
<link rel="stylesheet" href="https://fonts.googleapis.com/css2?family=Dancing+Script:wght@500&family=Poppins:wght@300&display=swap">
<style>
  :root {
    --page-bg: #efe6da;
    --card-black: #1d1d1e;
    --gold: #d9b07a;
    --gold-light: #fbe7d2;
    --gold-deep: #b88b55;
  }
  * { margin: 0; padding: 0; box-sizing: border-box; }
  html, body {
    width: 1200px;
    height: 1000px;
    overflow: hidden;
    background: var(--page-bg);
  }
  .business-card {
    position: absolute;
    left: 100px;
    top: 214px;
    width: 1000px;
    height: 572px;
    background: var(--card-black);
    border-radius: 4px;
    box-shadow: 0 10px 30px rgba(0,0,0,0.18);
  }
  .brand-name {
    position: absolute;
    left: 0;
    width: 820px;
    top: 120px;
    text-align: center;
    font-family: "Dancing Script", cursive;
    font-weight: 500;
    font-size: 88px;
    letter-spacing: 2px;
    color: var(--gold);
  }
  .contact-block {
    position: absolute;
    left: 0;
    width: 820px;
    top: 290px;
    text-align: center;
    font-family: "Poppins", sans-serif;
    font-weight: 300;
    color: var(--gold);
  }
  .person-name {
    font-size: 26px;
    letter-spacing: 1px;
    line-height: 1.2;
  }
  .person-role {
    font-size: 18px;
    letter-spacing: 1px;
    margin-bottom: 22px;
  }
  .contact-line {
    font-size: 19px;
    line-height: 1.35;
    letter-spacing: 0.5px;
  }
  .dress-illustration {
    position: absolute;
    left: 810px;
    top: 130px;
    width: 150px;
    height: 250px;
    border-radius: 40% 40% 8% 8% / 30% 30% 8% 8%;
    background: linear-gradient(180deg, var(--gold-light) 0%, var(--gold) 55%, var(--gold-deep) 100%);
    opacity: 0.9;
  }
</style>
</head>
<body>
  <section class="business-card">
    <h1 class="brand-name">Lustria Inc.</h1>

    <div class="contact-block">
      <p class="person-name">Maren Holtby</p>
      <p class="person-role">fashion stylist</p>
      <p class="contact-line">Tel: 403-555-0147</p>
      <p class="contact-line">Mail: hello@lustria.com</p>
      <p class="contact-line">Web: lustriastyle.com</p>
    </div>

    <div class="dress-illustration" role="img" aria-label="Gold foil sketch of a woman in a long evening gown"></div>
  </section>
</body>
</html>
```